Business Card Design

We custom build & and install Air filtration systems for mining machines - the system filters the air going into the cabin to protect the operator/driver Examples of the machines we install our units to would be Ironbadger or Hirosane. Australian owned company Our company colors are sky blue with polished Stainless steel lettering & framing. I have a logo which I will upload but I would like the new image to be crisper.

Industry/Entity Type

Business

Contact Information for Business Card

Company name - Cleanvent Pty Ltd
Paul Merriday - Position - Sales & Product Development Contact numbers Mob 0492 385 261 Tel - 07 3918 4526
Address - 147 Wexley Rd, Archerfield, Brisbane 4108, Australia

Colors
0255a3

Requirements
Must have
• sky blue & polished chrome lettering

```html
<!DOCTYPE html>
<html lang="en">
<head>
<meta charset="utf-8">
<title>Cleanvent Business Card</title>
<link rel="stylesheet" href="https://fonts.googleapis.com/css2?family=Michroma&display=swap">
<style>
  :root {
    --backdrop: #8e8e8e;
    --card-white: #f4f4f4;
    --brand-blue: #24419a;
    --band-shadow: #c9ccd3;
    --ink: #2a2a2a;
    --icon: #ffffff;
  }
  html, body {
    margin: 0;
    width: 1200px;
    height: 895px;
    overflow: hidden;
    background: var(--backdrop);
  }
  .card {
    position: absolute;
    left: 100px;
    top: 162px;
    width: 1000px;
    height: 571px;
    background: var(--card-white);
    box-shadow: 0 10px 30px rgba(0,0,0,0.3);
  }
  .card svg { display: block; width: 100%; height: 100%; }
  .band { fill: var(--brand-blue); }
  .band-edge { fill: var(--band-shadow); }
  .icon { fill: none; stroke: var(--icon); stroke-width: 3; }
  .icon-solid { fill: var(--icon); }
  .brand-name { font-family: "Michroma", sans-serif; font-size: 56px; fill: var(--brand-blue); }
  .info { font-family: "Michroma", sans-serif; font-size: 17px; fill: var(--ink); }
  .person { font-family: "Michroma", sans-serif; font-size: 23px; fill: var(--ink); letter-spacing: 2px; }
  .role { font-family: "Michroma", sans-serif; font-size: 10px; fill: var(--ink); letter-spacing: 0.5px; }
</style>
</head>
<body>
<div class="card">
  <svg viewBox="0 0 1000 571" xmlns="http://www.w3.org/2000/svg">
    <!-- brand -->
    <text class="brand-name" x="40" y="100">Cleanvent</text>

    <!-- stepped bands -->
    <polygon class="band-edge" points="0,190 330,190 358,163 330,136 338,136 366,163 338,194 0,194"/>
    <polygon class="band" points="0,140 330,140 356,165 330,190 0,190"/>

    <polygon class="band-edge" points="340,290 655,290 683,263 655,236 663,236 691,263 663,294 340,294"/>
    <polygon class="band" points="340,240 655,240 681,265 655,290 340,290 366,265"/>

    <polygon class="band" points="665,340 1000,340 1000,390 665,390 691,365"/>

    <polygon class="band-edge" points="0,478 420,478 430,470 420,470 0,470"/>
    <polygon class="band" points="0,480 420,480 470,571 0,571"/>

    <!-- globe icon -->
    <g transform="translate(110,165)">
      <circle class="icon" r="14"/>
      <ellipse class="icon" rx="6" ry="14"/>
      <line class="icon" x1="-14" y1="0" x2="14" y2="0"/>
      <line class="icon" x1="-12" y1="-7" x2="12" y2="-7"/>
      <line class="icon" x1="-12" y1="7" x2="12" y2="7"/>
    </g>

    <!-- pin icon -->
    <g transform="translate(500,265)">
      <path class="icon-solid" d="M0,16 C-4,8 -11,2 -11,-5 A11,11 0 0 1 11,-5 C11,2 4,8 0,16 Z"/>
      <circle cx="0" cy="-5" r="4" fill="var(--brand-blue)"/>
    </g>

    <!-- phone icon -->
    <g transform="translate(830,365)">
      <rect class="icon" x="-9" y="-16" width="18" height="32" rx="3"/>
      <line class="icon" x1="-9" y1="10" x2="9" y2="10"/>
    </g>

    <!-- contact -->
    <text class="info" x="30" y="235">hello@cleanvent.example</text>
    <text class="info" x="30" y="262">www.cleanvent.example</text>

    <text class="info" x="360" y="335">147 Wexley Rd</text>
    <text class="info" x="360" y="362">Archerfield QLD 4108</text>

    <text class="person" x="712" y="272">ALAN WHITBY</text>
    <text class="role" x="714" y="298">SALES &amp; PRODUCT DEVELOPMENT</text>

    <text class="info" x="690" y="440">0492 385 261</text>
    <text class="info" x="690" y="467">07 3918 4526</text>
  </svg>
</div>
</body>
</html>
```